Email Banner (QuillStacks)

We require an email banner for our email promotions sent to prospect clients. The banner needs to contain the wording QuillStacks and use the same colour scheme as the logos attached.

This is for B2B professional's so needs to look like a place you would come to read technology articles.

```html
<!DOCTYPE html>
<html lang="en">
<head>
<meta charset="utf-8">
<title>QuillStacks Email Banners</title>
<link href="https://fonts.googleapis.com/css2?family=Montserrat:wght@600;700;800&family=Lexend:wght@600&display=swap" rel="stylesheet">
<style>
  :root {
    --navy: #0b2a5c;
    --navy-deep: #071a3c;
    --ink: #0d1433;
    --red: #d9141b;
    --white: #ffffff;
    --paper: #ffffff;
    --rule: rgba(255,255,255,0.75);
  }
  html, body {
    margin: 0;
    padding: 0;
    width: 1200px;
    height: 960px;
    overflow: hidden;
    background: var(--paper);
    font-family: "Montserrat", Arial, sans-serif;
  }
  .canvas { position: relative; width: 1200px; height: 960px; }

  .banner {
    position: absolute;
    background: var(--navy);
    box-shadow: 9px 9px 7px rgba(0,0,0,0.38);
    overflow: hidden;
    color: var(--white);
  }
  .banner--wide { left: 114px; top: 160px; width: 988px; height: 246px; }
  .banner--stacked { left: 120px; top: 461px; width: 982px; height: 249px; }

  .banner__backdrop { position: absolute; inset: 0; }
  .dot-texture {
    position: absolute;
    top: 0; left: 30px;
    width: 60px; height: 100%;
    background: linear-gradient(180deg, rgba(40,80,150,0.55), rgba(40,80,150,0.05));
  }

  .info__title {
    position: absolute;
    margin: 0;
    font-weight: 800;
    font-size: 20px;
    letter-spacing: 0.2px;
    text-align: center;
  }
  .info__body {
    position: absolute;
    margin: 0;
    font-weight: 700;
    text-align: justify;
  }

  .banner--wide .info__title { left: 114px; width: 460px; top: 134px; }
  .banner--wide .info__body {
    left: 114px; width: 460px; top: 160px;
    font-size: 14.4px; line-height: 20.5px;
    text-align-last: justify;
  }
  .banner--stacked .info__title { left: 102px; width: 366px; top: 27px; }
  .banner--stacked .info__body {
    left: 102px; width: 366px; top: 64px;
    font-size: 13.6px; line-height: 18.6px;
  }

  .brand {
    position: absolute;
    display: flex;
    align-items: center;
    gap: 18px;
    color: var(--ink);
    font-family: "Lexend", "Montserrat", sans-serif;
    font-weight: 600;
  }
  .brand__mark { background: var(--red); flex: none; }
  .banner--wide .brand { left: 168px; top: 10px; font-size: 76px; letter-spacing: -1px; }
  .banner--wide .brand__mark { width: 46px; height: 46px; }
  .banner--stacked .brand {
    right: 36px; top: 12px; font-size: 66px; line-height: 66px;
    align-items: flex-end; letter-spacing: -0.5px;
  }
  .banner--stacked .brand__name { text-align: right; }
  .banner--stacked .brand__mark { width: 42px; height: 42px; margin-bottom: 10px; }

  .contacts {
    position: absolute;
    display: flex;
    align-items: stretch;
    list-style: none;
    margin: 0; padding: 0;
  }
  .contacts__item {
    display: flex;
    flex-direction: column;
    align-items: center;
    justify-content: flex-end;
    gap: 4px;
    padding: 0 12px;
    font-weight: 700;
    font-size: 14px;
    border-left: 1.5px solid var(--rule);
  }
  .contacts__item:first-child { border-left: none; }
  .contacts__icon { width: 18px; height: 18px; fill: none; stroke: var(--white); stroke-width: 1.6; }
  .contacts__handle { font-size: 12.5px; }
  .banner--wide .contacts { left: 600px; top: 170px; height: 48px; }
  .banner--stacked .contacts { left: 568px; top: 198px; height: 44px; }
  .banner--stacked .contacts__item { font-size: 13px; }
  .banner--stacked .contacts__handle { font-size: 11.5px; }
</style>
</head>
<body>
<main class="canvas">

  <section class="banner banner--wide">
    <svg class="banner__backdrop" viewBox="0 0 988 246" preserveAspectRatio="none" aria-hidden="true">
      <defs>
        <linearGradient id="navyWide" x1="0" x2="1">
          <stop offset="0" stop-color="#071a3c"/>
          <stop offset="0.35" stop-color="#0b2a5c"/>
        </linearGradient>
      </defs>
      <rect width="988" height="246" fill="url(#navyWide)"/>
      <path d="M108 0 H988 V182 C975 140 955 122 920 122 H168 C130 122 108 100 108 60 Z" fill="#ffffff"/>
    </svg>
    <div class="dot-texture" role="img" aria-label="Fading dot pattern"></div>

    <div class="brand">
      <span class="brand__mark"></span>
      <span class="brand__name">QuillStacks</span>
    </div>

    <h2 class="info__title">BANNER INFORMATION</h2>
    <p class="info__body">Lorem ipsum dolor sit amet, consectetuer adipiscing elit, sed diam nonummy nibh euismod tincidunt ut laoreet dolore magna aliquam erat volutpat. Ut wisi</p>

    <ul class="contacts">
      <li class="contacts__item">
        <svg class="contacts__icon" viewBox="0 0 24 24"><path d="M5 3h4l2 5-3 2a11 11 0 0 0 6 6l2-3 5 2v4a2 2 0 0 1-2 2A17 17 0 0 1 3 5a2 2 0 0 1 2-2z"/></svg>
        <span>Phone</span>
      </li>
      <li class="contacts__item">
        <svg class="contacts__icon" viewBox="0 0 24 24"><rect x="2.5" y="5" width="19" height="14"/><path d="M2.5 5l9.5 8 9.5-8"/></svg>
        <span>E mail</span>
      </li>
      <li class="contacts__item">
        <svg class="contacts__icon" viewBox="0 0 24 24"><circle cx="12" cy="12" r="9.5"/><ellipse cx="12" cy="12" rx="4" ry="9.5"/><path d="M2.5 12h19"/></svg>
        <span>Website</span>
      </li>
      <li class="contacts__item">
        <span class="contacts__handle">@quillstacks</span>
      </li>
    </ul>
  </section>

  <section class="banner banner--stacked">
    <svg class="banner__backdrop" viewBox="0 0 982 249" preserveAspectRatio="none" aria-hidden="true">
      <defs>
        <linearGradient id="navyStacked" x1="0" x2="1">
          <stop offset="0" stop-color="#071a3c"/>
          <stop offset="0.4" stop-color="#0b2a5c"/>
        </linearGradient>
      </defs>
      <rect width="982" height="249" fill="url(#navyStacked)"/>
      <path d="M486 0 H982 V223 C972 205 955 193 925 193 H530 C502 193 486 177 486 150 Z" fill="#ffffff"/>
    </svg>
    <div class="dot-texture" role="img" aria-label="Fading dot pattern"></div>

    <h2 class="info__title">BANNER INFORMATION</h2>
    <p class="info__body">Lorem ipsum dolor sit amet, consectetuer adipiscing elit, sed diam nonummy nibh euismod tincidunt ut laoreet dolore magna aliquam erat volutpat. Ut wisi enim ad minim. Lorem ipsum dolor sit amet, consectetuer adipiscing elit, sed diam nonummy nibh euismod tincidunt ut laoreet dolore magna aliquam erat volutpat. Ut wisi enim ad minim</p>

    <div class="brand">
      <span class="brand__mark"></span>
      <span class="brand__name">Quill<br>Stacks</span>
    </div>

    <ul class="contacts">
      <li class="contacts__item">
        <svg class="contacts__icon" viewBox="0 0 24 24"><path d="M5 3h4l2 5-3 2a11 11 0 0 0 6 6l2-3 5 2v4a2 2 0 0 1-2 2A17 17 0 0 1 3 5a2 2 0 0 1 2-2z"/></svg>
        <span>Phone</span>
      </li>
      <li class="contacts__item">
        <svg class="contacts__icon" viewBox="0 0 24 24"><rect x="2.5" y="5" width="19" height="14"/><path d="M2.5 5l9.5 8 9.5-8"/></svg>
        <span>E mail</span>
      </li>
      <li class="contacts__item">
        <svg class="contacts__icon" viewBox="0 0 24 24"><circle cx="12" cy="12" r="9.5"/><ellipse cx="12" cy="12" rx="4" ry="9.5"/><path d="M2.5 12h19"/></svg>
        <span>Website</span>
      </li>
      <li class="contacts__item">
        <span class="contacts__handle">@quillstacks</span>
      </li>
    </ul>
  </section>

</main>
</body>
</html>
```